Brochure design for Velicor

Create a bi-fold A5 size brochure. I have attached our logo and the written content to be included in the brochure. So the brochure will have a total of 4 pages (front page, inner two pages, back page). End source files need to include final printable brochure as well as editable files.

```html
<!DOCTYPE html>
<html lang="en">
<head>
<meta charset="utf-8">
<title>Velicor – A5 bi-fold brochure</title>
<link rel="stylesheet" href="https://fonts.googleapis.com/css2?family=Roboto:wght@400;500;700;900&display=swap">
<style>
  :root{
    --blue:#1466b0;
    --blue-deep:#0d4f91;
    --green:#5fae3e;
    --ink:#1b1b1b;
    --body:#2f2f2f;
    --rule:#d9dade;
    --paper:#ffffff;
    --stage:#a7a8ad;
  }
  *{box-sizing:border-box;margin:0;padding:0}
  html,body{width:1200px;height:1200px;overflow:hidden}
  body{background:var(--stage);font-family:"Roboto",Arial,sans-serif;color:var(--body);position:relative}

  .spread{position:absolute;display:flex;background:var(--paper)}
  .spread--outer{left:260px;top:30px;width:680px;height:481px}
  .spread--inner{left:200px;top:545px;width:800px;height:566px}
  .page{position:relative;background:var(--paper);overflow:hidden}
  .spread--outer .page{width:340px;height:481px}
  .spread--inner .page{width:400px;height:566px}
  .page + .page{border-left:1px solid #e4e5e8}

  .brand{position:absolute;font-weight:500;font-size:20px;color:var(--green);letter-spacing:-.3px}
  .photo{position:absolute}

  /* front cover */
  .cover__tagline{position:absolute;left:25px;top:22px;font-size:11px;font-weight:500;color:var(--ink);line-height:1.2}
  .cover__tagline strong{display:block;color:var(--blue);font-weight:700;letter-spacing:.2px}
  .cover .brand{left:222px;top:18px}
  .cover__photo{left:25px;top:80px;width:315px;height:240px;
    background:radial-gradient(circle at 55% 45%,#eaf4f7 0%,#a9cdd6 35%,#5f96a6 70%,#2f5f72 100%)}
  .cover__strip{position:absolute;left:25px;top:80px;width:10px;height:143px;background:var(--blue)}
  .cover__bar{position:absolute;left:178px;top:74px;width:127px;height:7px;background:var(--blue)}
  .cover__panel{position:absolute;left:178px;top:308px;width:127px;height:130px;background:var(--blue);color:#fff;padding:14px 12px}
  .cover__panel p{font-size:11px;line-height:1.3}
  .cover__panel h2{font-size:19px;font-weight:700;line-height:.98;margin-top:6px;letter-spacing:.2px}
  .cover__intro{position:absolute;left:27px;top:350px;width:145px;font-size:10px;font-weight:700;letter-spacing:.4px;color:var(--ink);line-height:1.3}
  .cover__rule{position:absolute;left:27px;top:384px;width:137px;height:2px;background:var(--blue)}
  .cover__headline{position:absolute;left:27px;top:392px;font-size:23px;font-weight:700;color:var(--blue);line-height:1;letter-spacing:1.2px}

  /* back cover */
  .back .brand{left:14px;top:12px}
  .back__photo{left:0;top:78px;width:170px;height:240px;background:linear-gradient(135deg,#c9a27e 0%,#e8c9b0 40%,#9aa8b6 75%,#5b6b7a 100%)}
  .back__panel{position:absolute;left:170px;top:78px;width:170px;height:146px;background:var(--blue);color:#fff;padding:10px 10px;font-size:6.6px;line-height:1.35}
  .back__panel p + p{margin-top:7px}
  .refs{position:absolute;left:10px;top:332px;right:22px}
  .refs .section-head{width:150px}
  .refs ol{margin-top:7px;padding-left:10px;font-size:5.6px;line-height:1.5;color:#333}
  .refs .note{font-size:5.6px;margin-top:1px}

  /* shared section head */
  .section-head{background:#e7e8ea;border-left:3px solid var(--blue);font-size:7px;font-weight:700;letter-spacing:.6px;text-transform:uppercase;color:var(--ink);padding:2px 6px;margin-bottom:5px}

  /* inner spread */
  .grid{position:absolute;inset:11px 0 0 0;display:grid;grid-template-columns:1fr 1fr;column-gap:0}
  .col{display:flex;flex-direction:column}
  .block{overflow:hidden}
  .text-block{padding:0 8px 4px 10px}
  .text-block p{font-size:6.4px;line-height:1.32;color:var(--body)}
  .page--left .col:first-child .text-block{padding-left:12px}

  .img-dna-blue{background:linear-gradient(160deg,#e8ecf2 0%,#b9c6dc 45%,#6f8fc6 75%,#e9edf4 100%)}
  .img-office{background:linear-gradient(120deg,#e9ecef 0%,#c8cdd2 50%,#8a939c 100%)}
  .img-code{background:linear-gradient(180deg,#1f2a8a 0%,#3a49c4 45%,#5ac1b8 70%,#1a237a 100%)}
  .img-body{background:radial-gradient(circle at 55% 55%,#2d6fb8 0%,#154a8c 45%,#0a2a5a 100%)}
  .img-helix-green{background:radial-gradient(circle at 60% 40%,#d9eadf 0%,#8fc3a3 45%,#3f8a6b 100%)}
  .img-kitchen{background:linear-gradient(120deg,#b48a62 0%,#d9b894 45%,#7b5a3e 100%)}
  .img-family{background:linear-gradient(120deg,#eef0f2 0%,#d6b9a3 50%,#8a6a55 100%)}
  .band-helix{position:absolute;left:0;right:0;bottom:0;height:59px;background:linear-gradient(90deg,#cfe6f3 0%,#5fa9d4 45%,#2a7fbe 70%,#d8ecf6 100%)}
  .fold{position:absolute;left:399px;top:0;width:2px;height:566px;background:linear-gradient(90deg,rgba(0,0,0,.08),rgba(0,0,0,0))}
</style>
</head>
<body>

<!-- Outer spread: back cover + front cover -->
<section class="spread spread--outer">
  <article class="page back">
    <div class="brand">Velicor</div>
    <div class="photo back__photo" role="img" aria-label="Photo of three colleagues looking at a computer screen in a bright studio"></div>
    <div class="back__panel">
      <p>For more information about Velicor or our products, please talk to your local retailer or email us at enquiries@velicor.co</p>
      <p>Please note test availability may differ from region to region and is subject to availability. Please talk to your local retailer for more information.</p>
      <p>For a list of approved Velicor retailers please visit www.velicor.co</p>
    </div>
    <div class="refs">
      <div class="section-head">References</div>
      <ol>
        <li>Genome consortium release: human genome project completed, 2003.</li>
        <li>Review: clinical application of pharmacogenetics, 2001.</li>
        <li>Study of pharmacogenetics, 1998.</li>
        <li>Journal of molecular diagnostics, 2016.</li>
        <li>Clinical pharmacology and therapeutics, 2016.</li>
        <li>Pharmacogenomics and personalised medicine, 2017.</li>
        <li>Clinical pharmacology and therapeutics, 2014.</li>
        <li>Food elimination in irritable bowel syndrome: controlled trial, 2004.</li>
        <li>Controlled trial of food elimination in migraine, 2011.</li>
        <li>Food allergy and migraine, 2007.</li>
        <li>Immune complexes in food-induced arthralgia, 1987.</li>
      </ol>
      <p class="note">• Additional fees may apply.</p>
    </div>
  </article>

  <article class="page cover">
    <p class="cover__tagline">We’re helping to build the <strong>FUTURE OF GOOD HEALTH</strong></p>
    <div class="brand">Velicor</div>
    <div class="photo cover__photo" role="img" aria-label="Close-up photo of a pipette dropping liquid into laboratory glassware"></div>
    <div class="cover__strip"></div>
    <div class="cover__bar"></div>
    <div class="cover__panel">
      <p>Precision health and wellness is tailored to your</p>
      <h2>UNIQUE GENETIC MAKE-UP</h2>
    </div>
    <p class="cover__intro">A revolution in health &amp; wellness has been brewing</p>
    <div class="cover__rule"></div>
    <h1 class="cover__headline">AND NOW<br>IT IS HERE</h1>
  </article>
</section>

<!-- Inner spread -->
<section class="spread spread--inner">
  <article class="page page--left">
    <div class="grid">
      <div class="col">
        <div class="block text-block" style="height:118px">
          <div class="section-head">Precision health &amp; wellness</div>
          <p>You are unique. Your healthcare and lifestyle decisions need to be tailored to you. Ever since the human genome was decoded, a plethora of scientific data has revealed everything from disease-causing genes to genetically tailored diets. We all want to live longer and healthier lives, whilst performing at our peak. One size does not fit all and the only way to find out what’s right for you is to unlock your hidden code.</p>
        </div>
        <div class="block photo-cell img-dna-blue" style="height:143px" role="img" aria-label="Illustration of a blue and orange DNA double helix"></div>
        <div class="block text-block" style="height:107px;padding-top:5px">
          <div class="section-head">Unlock your hidden code</div>
          <p>A whole new world of discovery awaits with the Velicor range of genetic testing services. From unlocking your complete genome with Whole Genome Sequencing (WGS) to just learning about specific aspects of what makes you… you. With Velicor, you can find answers to the questions that can help you to live a healthier, longer and optimal quality of life.</p>
        </div>
        <div class="block img-body" style="height:187px" role="img" aria-label="Digital illustration of a human body with highlighted digestive organs"></div>
      </div>
      <div class="col">
        <div class="block img-office" style="height:115px" role="img" aria-label="Photo of people working at desks in a bright office"></div>
        <div class="block text-block" style="height:148px;padding-top:5px">
          <div class="section-head">DNA – the code of life</div>
          <p>Every individual living organism has a completely unique set of DNA. Your DNA is the chemical blueprint that codes for everything in your body and is found in all of the trillions of cells that you are made of. Collections of DNA are called genes and the complete set of genes in an individual is referred to as their genome. The human genome was first decoded in 2003, taking over 13 years and $2.7 billion to complete. Thanks to exponential advances in technology, Velicor can now unlock your DNA for only a fraction of the time and cost.</p>
        </div>
        <div class="block img-code" style="height:104px" role="img" aria-label="Colourful visualisation of genetic sequence letters and bars"></div>
        <div class="block text-block" style="height:188px;padding-top:5px">
          <div class="section-head">DNA &amp; disease</div>
          <p>Prevention is better than any cure. Scientific studies have uncovered numerous genes associated with a range of cancers, heart conditions, and other common diseases affecting society today. The range of genetic tests available through Velicor can now identify if these, and other, genes are present in you. This allows you and your physician to potentially prevent, manage, monitor and treat relevant conditions. Furthermore, as the rapid pace of science continues to uncover new genes related to disease, Velicor can quickly update you and your doctor with the latest research and what it means for you.</p>
        </div>
      </div>
    </div>
  </article>

  <article class="page page--right">
    <div class="grid">
      <div class="col">
        <div class="block text-block" style="height:212px">
          <div class="section-head">DNA &amp; drugs</div>
          <p>Scientific research has shown that the response rate for many prescribed drugs is as low as 50% and that genetic factors can account for up to 95% of drug-response variability and susceptibility. In other words, many of the drugs you take in your lifetime will likely be inadequately dosed, leading to potential side effects or no effects at all. With Velicor, you and your doctor can proactively identify appropriate types, and dosages, for a range of prescribed and over-the-counter medications. This includes medications you currently take and any common future medications you are likely to encounter at some stage in your life. A number of studies have shown that over 74% of people taking a genetic test for medication compatibility learned information that is relevant to them.</p>
        </div>
        <div class="block img-kitchen" style="height:146px" role="img" aria-label="Photo of a couple preparing food together in a kitchen"></div>
        <div class="block text-block" style="height:110px;padding-top:5px">
          <div class="section-head">DNA &amp; descent</div>
          <p>The discipline of genealogy has exploded over recent years with the advent of DNA testing. The Velicor range of tests can help you track and understand your ancestry and paternity tests can help identify an individual’s biological father. Family planning tests can help identify a couple’s risk profile for conceiving children with any of the dozens of known genetic conditions that can affect humans.</p>
        </div>
      </div>
      <div class="col">
        <div class="block img-helix-green" style="height:207px" role="img" aria-label="Illustration of a green DNA helix with capsules"></div>
        <div class="block text-block" style="height:150px;padding-top:5px">
          <div class="section-head">DNA &amp; diet</div>
          <p>Certain foods are thought to inappropriately cause immune reactions in genetically predisposed individuals. This can result in symptoms like fatigue, bloating, bowel disturbances, headaches, migraines, joint aches, eczema or acne. DNA testing can help identify such foods as well as genes associated with the metabolism and absorption of vitamins, minerals and stimulants like coffee. The Velicor range of tests can even help create precision diet and fitness plans based on your genes and goals.</p>
        </div>
        <div class="block img-family" style="height:111px" role="img" aria-label="Photo of a smiling family with a baby"></div>
      </div>
    </div>
    <div class="band-helix" role="img" aria-label="Panoramic illustration of a blue DNA helix"></div>
  </article>
  <div class="fold"></div>
</section>

</body>
</html>
```